Now Leasing Banner

Looking for a banner that says the following information approx 4' x 30'

Now Leasing Maplewood Terrace 925-318-6054

Target Market(s)

Drive by traffic

Industry/Entity Type

Residential property management

Requirements
Must have
• Clear and readable from a distance

```html
<!DOCTYPE html>
<html lang="en">
<head>
<meta charset="utf-8">
<title>Now Leasing – Maplewood Terrace</title>
<link rel="stylesheet" href="https://fonts.googleapis.com/css2?family=Oswald:wght@700&display=swap">
<style>
  :root {
    --bg-page: #1b1b1b;
    --aerial-dark: #2c2f27;
    --aerial-mid: #3f4536;
    --aerial-light: #4d5440;
    --disc: #1c1c1c;
    --text-light: #ffffff;
    --text-accent: #e4ff00;
    --shadow: rgba(0, 0, 0, 0.75);
  }
  html, body {
    margin: 0;
    padding: 0;
    width: 1200px;
    height: 160px;
    overflow: hidden;
    background: var(--bg-page);
  }
  .banner {
    display: block;
    width: 1200px;
    height: 160px;
  }
  .aerial-view { fill: url(#aerialTones); }
  .center-disc { fill: var(--disc); }
  .headline {
    font-family: 'Oswald', 'Arial Narrow', sans-serif;
    font-weight: 700;
    font-size: 72px;
    filter: drop-shadow(2px 2px 2px var(--shadow));
  }
  .headline--light { fill: var(--text-light); }
  .headline--accent { fill: var(--text-accent); }
</style>
</head>
<body>
<svg class="banner" viewBox="0 0 1200 160" xmlns="http://www.w3.org/2000/svg">
  <defs>
    <linearGradient id="aerialTones" x1="0" y1="0" x2="1" y2="1">
      <stop offset="0" stop-color="var(--aerial-mid)"/>
      <stop offset="0.35" stop-color="var(--aerial-dark)"/>
      <stop offset="0.7" stop-color="var(--aerial-light)"/>
      <stop offset="1" stop-color="var(--aerial-dark)"/>
    </linearGradient>
  </defs>

  <rect class="aerial-view" x="0" y="0" width="1200" height="160"
        role="img" aria-label="Darkened aerial photo of the apartment community, hillside neighborhoods and highway"/>

  <circle class="center-disc" cx="567" cy="80" r="200"/>

  <text class="headline headline--light" x="30" y="106"
        textLength="333" lengthAdjust="spacingAndGlyphs">Now Leasing</text>
  <text class="headline headline--light" x="382" y="106"
        textLength="372" lengthAdjust="spacingAndGlyphs">Maplewood Terrace</text>
  <text class="headline headline--accent" x="776" y="106"
        textLength="400" lengthAdjust="spacingAndGlyphs">925-318-6054</text>
</svg>
</body>
</html>
```